New website

We ned to create a new website that reflects more who we are. We are delivering exclusive premium products to our customers and the current website does not reflect our products at all.
We believe in less is more and need a webpage that is clean yet professional and exclusive.

Target Market(s)

Dentistry

Industry/Entity Type

Dental

Number of Pages Required

5+ page

Font styles to use
Sans Serif

Colors

Designer to choose colors to be used in the design.

Requirements
Must have
• Picture gallery
• Nice structure
• Clean layout
Nice to have
• Light fonts
Should not have
• Any italic font styles

```html
<!DOCTYPE html>
<html lang="en">
<head>
<meta charset="utf-8">
<title>Lumen Dent</title>
<link rel="stylesheet" href="https://fonts.googleapis.com/css2?family=Raleway:wght@300;400;500;600;700;800&family=Montserrat:wght@600;700&display=swap">
<style>
:root{
  --hero-deep:#0a3f8f;
  --hero-mid:#1561b0;
  --hero-light:#2a86c8;
  --navy:#163a66;
  --ink:#1d4a7a;
  --body:#4b5f78;
  --pink:#e0969a;
  --red:#c64c4c;
  --card:#ffffff;
  --feature-bg:#f3f7fb;
  --feature-line:#dbe6f1;
  --dot:#1a63ad;
  --footer:#0a67b0;
  --footer-bar:#0b4a7a;
  --accent:#e36a6a;
  --white:#ffffff;
}
*{margin:0;padding:0;box-sizing:border-box}
html,body{width:1094px;height:1200px;overflow:hidden;background:var(--white)}
body{position:relative;font-family:'Raleway',sans-serif;color:var(--body)}
.abs{position:absolute}

.hero{left:0;top:0;width:1094px;height:376px;
  background:radial-gradient(ellipse at 55% 45%,var(--hero-light) 0%,var(--hero-mid) 40%,var(--hero-deep) 85%)}
.brand{left:0;top:20px;width:1094px;text-align:center;color:var(--white);
  font-family:'Raleway',sans-serif;font-weight:400;font-size:14px;letter-spacing:7px}
.brand-mark{display:inline-block;width:10px;height:10px;background:var(--white);margin-right:10px;vertical-align:1px}
.nav{left:0;top:73px;width:1094px;display:flex;justify-content:center;gap:27px;
  font-family:'Montserrat',sans-serif;font-weight:700;font-size:8.5px;color:var(--white);letter-spacing:.4px}
.hero-title{left:0;top:112px;width:1094px;text-align:center;color:var(--white);
  font-weight:700;font-size:40px;line-height:42px;letter-spacing:-1.8px}
.hero-text{left:327px;top:214px;width:440px;text-align:center;color:var(--white);
  font-weight:600;font-size:11.2px;line-height:14.4px}
.btn-pink{background:var(--pink);color:var(--white);text-align:center;font-weight:600;letter-spacing:-.2px}
.hero-btn{left:452px;top:282px;width:190px;height:22px;line-height:22px;font-size:10.5px;border-radius:2px}

.categories{left:137px;top:349px;width:821px;height:179px;background:var(--card);
  box-shadow:0 1px 4px rgba(20,50,90,.1)}
.category{top:24px;width:160px;text-align:center}
.category svg{display:block;margin:0 auto;height:58px}
.category-name{margin-top:26px;font-weight:500;font-size:12px;color:var(--navy)}
.btn-red{display:inline-block;margin-top:8px;width:99px;height:23px;line-height:23px;background:var(--red);
  color:var(--white);font-weight:700;font-size:7.6px;border-radius:2px;letter-spacing:-.1px}

.feature{top:555px;width:396px;height:136px;background:var(--feature-bg);border:1px solid var(--feature-line)}
.feature-label{left:13px;top:15px;font-weight:700;font-size:7.5px;color:var(--navy)}
.feature-title{left:13px;top:27px;font-weight:400;font-size:13px;color:var(--navy);font-variant:small-caps;letter-spacing:1px}
.feature-text{left:13px;top:51px;width:200px;font-weight:400;font-size:8.8px;line-height:14.4px;color:var(--body)}
.feature-photo{left:222px;top:14px;width:161px;height:108px}
.photo-dark{background:radial-gradient(ellipse at 50% 50%,#3a3f8c 0%,#14163a 55%,#050510 100%)}
.photo-light{background:linear-gradient(100deg,#eeeae6 0%,#dcd6d0 45%,#e8c9b4 75%,#f2ece8 100%)}

.dots{left:528px;top:718px;display:flex;gap:7px;align-items:center}
.dot{width:3px;height:3px;border-radius:50%;background:var(--dot)}
.dot.active{width:8px;height:8px;border:1px solid var(--dot);background:radial-gradient(circle,var(--dot) 0 1.6px,transparent 2px)}

.story{left:137px;top:751px;width:821px;height:269px;
  background:radial-gradient(ellipse at 55% 30%,#e9edf1 0%,#f3f4f6 45%,#fbfbfb 80%);
  box-shadow:0 1px 3px rgba(20,50,90,.06)}
.story-title{left:0;top:22px;width:821px;text-align:center;font-weight:300;font-size:27px;color:var(--ink)}
.story-text{left:180px;width:461px;text-align:center;font-weight:400;font-size:10.8px;line-height:16.5px;color:var(--body)}
.story-btn{left:329px;top:225px;width:163px;height:17px;line-height:17px;font-size:9px;border-radius:2px}

.footer{left:0;top:1047px;width:1094px;height:118px;background:var(--footer);color:var(--white)}
.footer-heading{top:31px;font-weight:400;font-size:12px;letter-spacing:.5px}
.footer-links{top:53px;font-family:'Montserrat',sans-serif;font-weight:700;font-size:7.6px;line-height:16.3px}
.footer-contact{top:53px;font-family:'Montserrat',sans-serif;font-weight:600;font-size:7.6px;line-height:13.5px}
.footer-bar{left:0;top:1165px;width:1094px;height:35px;background:var(--footer-bar);color:var(--white);
  text-align:center;font-size:8px;line-height:35px;font-weight:500}
.footer-bar .name{color:var(--accent);font-weight:600}
</style>
</head>
<body>

<header class="abs hero" role="img" aria-label="Blue-toned photo of a smiling woman lying on grass">
  <div class="abs brand"><span class="brand-mark"></span>LUMEN DENT</div>
  <nav class="abs nav"><span>HOME</span><span>PRODUCTS</span><span>SERVICES</span><span>SMILES</span><span>LUMEN DENT</span><span>CONTACT</span></nav>
  <h1 class="abs hero-title">Make Sweden more beautiful,<br>one smile at a time</h1>
  <p class="abs hero-text">Lumen Dent specializes in cosmetic and aesthetic dentistry. We satisfy our customers with fixed restorations, made with the help of modern science, precision and art. Our customers can expect work of the highest quality.</p>
  <div class="abs btn-pink hero-btn">CONTACT US</div>
</header>

<section class="abs categories">
  <div class="abs category" style="left:4px">
    <svg viewBox="0 0 30 58" fill="none" stroke="#5a9ad3" stroke-width="1.6"><rect x="8" y="1" width="14" height="8"/><rect x="8" y="9" width="14" height="47"/><line x1="8" y1="22" x2="22" y2="22"/><line x1="8" y1="40" x2="22" y2="40"/><line x1="15" y1="40" x2="15" y2="56"/><line x1="8" y1="46" x2="22" y2="46"/><line x1="8" y1="51" x2="22" y2="51"/></svg>
    <div class="category-name">Aethetics and Function</div>
    <span class="btn-red">VIEW PRODUCTS</span>
  </div>
  <div class="abs category" style="left:167px">
    <svg viewBox="0 0 50 58" fill="none" stroke="#5a9ad3" stroke-width="1.6"><path d="M8 8c6-5 12-1 16 1 5-2 10-5 15-1 4 4 3 14 0 20-2 5-2 12-4 20-1 6-6 6-6 0 0-6-1-12-4-12s-4 6-4 12c0 6-5 6-6 0-2-8-2-15-4-20-3-6-4-16 1-20z"/><path d="M42 2v10M37 7h10"/></svg>
    <div class="category-name">All-ceramics</div>
    <span class="btn-red">VIEW PRODUCTS</span>
  </div>
  <div class="abs category" style="left:330px">
    <svg viewBox="0 0 70 58" fill="none" stroke="#5a9ad3" stroke-width="1.6"><ellipse cx="35" cy="40" rx="33" ry="9"/><path d="M2 40v8c0 5 15 9 33 9s33-4 33-9v-8"/><circle cx="35" cy="18" r="14"/><circle cx="35" cy="18" r="8"/><circle cx="35" cy="18" r="3"/><rect x="27" y="32" width="16" height="10"/></svg>
    <div class="category-name">Diagnostics</div>
    <span class="btn-red">VIEW PRODUCTS</span>
  </div>
  <div class="abs category" style="left:493px">
    <svg viewBox="0 0 50 58" fill="none" stroke="#5a9ad3" stroke-width="1.6"><path d="M6 4c6-4 12 0 19 0s13-4 19 0c5 5 2 17-6 20H12C4 21 1 9 6 4z"/><rect x="17" y="24" width="16" height="6"/><path d="M18 30h14l-2 26h-10z"/><line x1="18" y1="37" x2="32" y2="37"/><line x1="19" y1="44" x2="31" y2="44"/><line x1="19" y1="50" x2="31" y2="50"/></svg>
    <div class="category-name">Implant</div>
    <span class="btn-red">VIEW PRODUCTS</span>
  </div>
  <div class="abs category" style="left:656px">
    <svg viewBox="0 0 50 58" fill="none" stroke="#5a9ad3" stroke-width="1.6"><path d="M6 6c6-6 13-2 19 0 6-2 13-6 19 0 5 6 2 18-2 24-2 6-2 14-5 22-1 5-5 5-6 0l-3-16-3 16c-1 5-5 5-6 0-3-8-3-16-5-22-4-6-7-18-2-24z"/><path d="M12 10c4-3 9 0 13 2 4-2 9-5 13-2"/></svg>
    <div class="category-name">Plastics</div>
    <span class="btn-red">VIEW PRODUCTS</span>
  </div>
</section>

<article class="abs feature" style="left:137px">
  <div class="abs feature-label">FEATURED PRODUCT</div>
  <h3 class="abs feature-title">Solidra</h3>
  <p class="abs feature-text">Lorem ipsum dolor sit amet, consectetur adipiscing elit. Vivamus vestibulum sed sem ut eleifend. Maecenas eleifend, mauris non aliquam consectetur, eros neque sollicitudin erat, eu</p>
  <div class="abs feature-photo photo-dark" role="img" aria-label="Full arch dental bridge on a dark reflective surface"></div>
</article>

<article class="abs feature" style="left:561px">
  <div class="abs feature-label">FEATURED PRODUCT</div>
  <h3 class="abs feature-title">Shade Finder</h3>
  <p class="abs feature-text">Lorem ipsum dolor sit amet, consectetur adipiscing elit. Vivamus vestibulum sed sem ut eleifend. Maecenas eleifend, mauris non aliquam consectetur, eros neque sollicitudin erat, eu</p>
  <div class="abs feature-photo photo-light" role="img" aria-label="Patient having tooth shade measured with an intraoral device"></div>
</article>

<div class="abs dots"><span class="dot active"></span><span class="dot"></span><span class="dot"></span><span class="dot"></span></div>

<section class="abs story" role="img" aria-label="Faded photo of a smiling woman giving thumbs up">
  <h2 class="abs story-title">We create smiles</h2>
  <p class="abs story-text" style="top:70px">Lumen Dent has over the years helped well over 10,000 patients with their smiles. Many of them may see every day without knowing it. &nbsp;Select a Lumen Dent smile the next time you are with, we have the knowledge and experience.</p>
  <p class="abs story-text" style="top:139px">Your natural teeth, you should try to nurture the best possible way. They are the finest and most precious of chewing function created - but they must also harmonize with your personality and appearance. We believe that a beautiful smile shapes and strengthens both your confidence and self esteem.</p>
  <div class="abs btn-pink story-btn">CONTACT US</div>
</section>

<footer class="abs footer">
  <div class="abs footer-heading" style="left:376px">Quick Links</div>
  <div class="abs footer-links" style="left:377px">HOME<br>PRODUCTS<br>SERVICES</div>
  <div class="abs footer-links" style="left:435px">SMILES<br>LUMEN DENT<br>CONTACT</div>
  <div class="abs footer-heading" style="left:519px">Contact</div>
  <div class="abs footer-contact" style="left:519px">Lumen Dent AB<br>Tel: 040-12 34 56</div>
  <div class="abs footer-contact" style="left:602px">PO Box 10234-22100 Lund,<br>Sweden</div>
</footer>
<div class="abs footer-bar">© 2017 <span class="name">lumendent</span> All Rights Reserved</div>

</body>
</html>
```